Realestate development- Flyer template

We are a real estate developer and we are about to commence construction of 8, 2 bedroom units in Perth Western Australia.
I need a single sided flyer (A4) to use at point of sale when we meet prospective buyers. We would like the design serve as a template for other projects in the future so that we achieve consistency in our marketing (i.e. I NEED TO BE ABLE TO CHANGE THE PICTURES AND TEXT) but layout stays the same.
It should have a minimum of 3 and a maximum of 5 places for images. Typically images used are of the exterior, the bathroom, bedrooms and living space/yard.

Our target market is first home buyers- single or married professionals 20-35 years old and/or investors.

The flyer template needs to make the best use of the images to motivate a reader to want to make a purchase. Typically we keep text to a minimum of facts and try to use emotive images to give a buyer a sense of connection with the property.

We need to convey that we are experienced, build a quality product and that our properties have that little bit more value than competitors.

We have a website www.harbenlotworks.com and i'd like the flyer to reflect the same colours/ style if possible (Green, Black, Brown). You can find out more about us on the website and also contact me there if needed.

Thanks!
Updates

Some text for the add:

From $338500
14 Maldrin Rd, Coltenby

Four 2 Bed x 2 Bath ground floor units with courtyard
Four 2 Bed x 1 Bath top floor units with balcony
Ensuite bathroom
Quality finish- 60m2 plus balcony/courtyard
Train: 900m
Brackwater Mall: 800m
Designated Car Bay

The area offers convenience to shops, schools, public transport and everything else you need. From Yarrowmere Collegiate School, Tenby Oaks College, the new Hospital and soon a University campus of up to 900 students. Let’s not forget everything the Corvel Basin has to offer, restaurants, wineries and breweries, quality food producers, wildlife parks, the list goes on and on.
Call us now and secure your new home or investment.

Target Market(s)

First home buyers and investors

Industry/Entity Type

Construction

Requirements
Must have
• Agent Contact details
Agent logo (Vessington Realty)
Company logo (Stonereach Developments)

Nice to have
• QR Code
Should not have
• Space to insert a cheesy photo of a realestate agent.

```html
<!DOCTYPE html>
<html lang="en">
<head>
<meta charset="utf-8">
<title>Stonereach Developments – 14 Maldrin Rd, Coltenby</title>
<link rel="stylesheet" href="https://fonts.googleapis.com/css2?family=Roboto+Condensed:wght@400;700&family=Roboto:wght@400;700&display=swap">
<style>
  :root{
    --charcoal:#3a3a3a;
    --charcoal-dark:#262626;
    --green:#6f9f3c;
    --green-dark:#4f7a26;
    --green-bar:#5c8a2e;
    --black:#111111;
    --white:#ffffff;
    --ink:#1c1c1c;
  }
  *{box-sizing:border-box;margin:0;padding:0}
  html,body{width:729px;height:1200px;overflow:hidden;background:var(--white)}
  .flyer{position:relative;width:729px;height:1200px;overflow:hidden;
    background:linear-gradient(180deg,var(--charcoal-dark) 0,var(--charcoal) 300px,var(--green) 300px,var(--green) 100%);
    font-family:"Roboto",Arial,sans-serif;color:var(--ink)}
  .brand{position:absolute;left:30px;top:26px;display:flex;align-items:center;gap:14px}
  .brand-mark{width:64px;height:64px;background:var(--green)}
  .brand-name{font-family:"Roboto Condensed","Arial Narrow",sans-serif;font-weight:700;color:var(--white);font-size:28px;line-height:1.05;letter-spacing:.5px}
  .brand-name span{display:block;font-size:13px;font-weight:700;letter-spacing:3px;margin-top:4px}
  .photo{position:absolute;border:6px solid var(--white);box-shadow:0 2px 6px rgba(0,0,0,.35)}
  .photo-exterior{left:50px;top:134px;width:656px;height:456px;
    background:linear-gradient(180deg,#6fa3d8 0%,#a9cdea 45%,#e9ece8 60%,#b9b7aa 80%,#7f8a5c 100%)}
  .photo-bedroom{left:42px;top:437px;width:276px;height:220px;
    background:linear-gradient(160deg,#d8d4cc 0%,#b7aea2 55%,#6a2a2a 80%,#3a2c26 100%)}
  .photo-dining{left:42px;top:692px;width:276px;height:210px;
    background:linear-gradient(160deg,#e7e0d3 0%,#b39c82 50%,#5a4634 100%)}
  .photo-living{left:42px;top:935px;width:276px;height:232px;
    background:linear-gradient(160deg,#f2f2ee 0%,#cfd6cc 50%,#7c8c6c 100%)}
  .price-box{position:absolute;left:328px;top:413px;width:378px;height:140px;background:var(--black);color:var(--white);padding:18px 26px}
  .price-from{font-family:"Roboto Condensed","Arial Narrow",sans-serif;font-weight:700;font-size:38px;line-height:1}
  .price-amount{font-family:"Roboto Condensed","Arial Narrow",sans-serif;font-weight:700;font-size:58px;line-height:1}
  .address{position:absolute;left:344px;top:560px;font-family:"Roboto Condensed","Arial Narrow",sans-serif;font-weight:700;font-size:24px;color:var(--black)}
  .features{position:absolute;left:328px;top:600px;width:378px;list-style:none}
  .features li{background:var(--green-bar);color:var(--white);font-size:15.5px;padding:4px 8px;margin-bottom:3px;border-bottom:1px solid var(--green-dark)}
  .area{position:absolute;left:330px;top:828px;width:372px;font-size:11.2px;line-height:1.42;color:var(--white)}
  .area strong{display:block;font-weight:700;font-style:italic;font-size:14.5px;line-height:1.3;margin-top:3px;color:var(--white)}
  .qr-slot{position:absolute;left:583px;top:962px;width:122px;height:140px;background:var(--white);border:3px solid var(--black)}
  .agent{position:absolute;left:583px;top:1105px;width:122px;background:var(--white);text-align:center;font-family:"Roboto Condensed","Arial Narrow",sans-serif;font-weight:700;font-size:20px;padding:2px 0;color:var(--black)}
  .office{position:absolute;left:330px;top:1107px;width:250px;font-size:9.5px;color:var(--white)}
  .contact{position:absolute;right:24px;top:1134px;text-align:right;font-family:"Roboto Condensed","Arial Narrow",sans-serif;font-weight:700;color:var(--black)}
  .phone{font-size:32px;line-height:1}
  .web{font-size:23px;font-style:italic;line-height:1.25}
</style>
</head>
<body>
<main class="flyer">
  <header class="brand">
    <div class="brand-mark"></div>
    <div class="brand-name">STONEREACH<br>DEVELOPMENTS<span>- PERTH, WA -</span></div>
  </header>

  <div class="photo photo-exterior" role="img" aria-label="Exterior view of the two-storey townhouse development"></div>
  <div class="photo photo-bedroom" role="img" aria-label="Furnished bedroom interior"></div>
  <div class="photo photo-dining" role="img" aria-label="Dining and kitchen area"></div>
  <div class="photo photo-living" role="img" aria-label="Open-plan living space"></div>

  <section class="price-box">
    <div class="price-from">From</div>
    <div class="price-amount">$338500</div>
  </section>
  <div class="address">14 Maldrin Rd, Coltenby</div>

  <ul class="features">
    <li>Four 2 Bed x 2 Bath ground floor units with courtyard</li>
    <li>Four 2 Bed x 1 Bath top floor units with balcony</li>
    <li>Ensuite bathroom</li>
    <li>Quality finish</li>
    <li>Train: 900m</li>
    <li>Brackwater Mall: 800m</li>
    <li>Designated Car Bay</li>
  </ul>

  <p class="area">The area offers convenience to shops, schools, public transport and everything else you need. From Yarrowmere Collegiate School, Tenby Oaks College, the new Hospital and soon a University campus of up to 900 students. Let’s not forget everything the Corvel Basin has to offer, restaurants, wineries and breweries, quality food producers, wildlife parks, the list goes on and on.
    <strong>Call us now and secure your new home or investment.</strong></p>

  <div class="qr-slot" aria-label="Space for QR code"></div>
  <div class="agent">Dale Morven</div>
  <div class="office">7/88 Calloway Street Perth WA 6000, Australia</div>

  <footer class="contact">
    <div class="phone">61 412 873 209</div>
    <div class="web">harbenlotworks.com</div>
  </footer>
</main>
</body>
</html>
```